Webdesign für Kleingruppenreisen in die Südsteiermark
Zielgruppe
Wir sind ein Start-Up Unternehmen, das als Kleingruppenreisen in die Südsteiermark veranstaltet; der Schwerpunkt liegt auf dem Kulinarischen. Zielgruppe sind Geschäftsleute, die diese Kurzreisen (Do-So) für Marketingzwecke oder als Mitarbeiterbonus (oder auch privat) nutzen möchten.
Aufgabenstellung
Die Homepage soll eine Online-Shop Möglichkeit bieten, in der die Reise (bisher gibt es nur einen Ablauf) gebucht werden kann. Optisch sollte sie sich an das bereits von Ihnen erstellte Logo anlehnen und möglichst ansprechende Fotos von der Südsteiermark, Hollerau, Leoben usw. enthalten. (Siehe die beiden Flyer und das Logo)
Wir haben inzwischen Bildfreigaben von Mirtler und dem Tourismusverband Hollerau erhalten und können auch eigene Bilder zur Verfügung stellen. Bitte kontaktieren Sie uns dafür, wenn nötig.

```html
<!DOCTYPE html>
<html lang="de">
<head>
<meta charset="utf-8">
<title>Genusspfade – Reisen für Feinschmecker</title>
<link rel="stylesheet" href="https://fonts.googleapis.com/css2?family=Open+Sans:ital,wght@0,300;0,400;0,600;0,700;1,400;1,600;1,700&family=Berkshire+Swash&display=swap">
<style>
:root{
  --wine:#a11c28;
  --wine-dark:#8e1822;
  --grey-bg:#e6e6e6;
  --btn-grey:#757575;
  --text:#222;
  --muted:#555;
  --white:#fff;
}
*{box-sizing:border-box;margin:0;padding:0}
html,body{width:1200px;height:2171px;overflow:hidden}
body{position:relative;font-family:"Open Sans",sans-serif;color:var(--text);background:var(--white)}
.abs{position:absolute}
.script{font-family:"Berkshire Swash",cursive}

.top-bar{left:0;top:0;width:1200px;height:37px;background:var(--wine)}
.header{left:0;top:37px;width:1200px;height:137px;background:var(--white)}
.brand{left:228px;top:86px;display:flex;align-items:center;gap:10px;font-size:30px;font-weight:700;line-height:36px;color:var(--wine)}
.brand-mark{width:22px;height:22px;border-radius:50%;background:var(--wine)}
.nav{left:461px;top:94px;display:flex;gap:20px;font-size:16px;line-height:22px;color:#666}
.nav .active{color:var(--wine)}
.search{left:944px;top:91px}

.hero{left:0;top:174px;width:1200px;height:450px;background:linear-gradient(90deg,#8a7a3e 0%,#b87f86 30%,#c68a8e 55%,#a45a4c 70%,#7d7a36 100%)}
.hero-title{left:0;top:345px;width:1200px;text-align:center;color:var(--white);font-size:40px;line-height:48px}
.hero-sub{left:0;top:394px;width:1200px;text-align:center;color:var(--white);font-size:30px;font-weight:300;line-height:40px}
.hero-btn{left:480px;top:481px;width:240px;height:53px;border:1px solid var(--white);color:var(--white);font-size:18px;font-weight:300;display:flex;align-items:center;justify-content:center}

.welcome{left:0;top:624px;width:1200px;height:406px;background:linear-gradient(90deg,#fff 0%,#fff 45%,#ececec 75%,#dedede 100%)}
.welcome-photo{left:800px;top:624px;width:400px;height:406px;background:radial-gradient(ellipse at 60% 45%,#a8b85a 0%,#c9b27a 35%,rgba(230,230,230,0) 70%)}
.welcome-title{left:105px;top:670px;font-size:26px;line-height:34px;color:#555}
.welcome-text{left:105px;top:720px;width:630px;font-size:12.2px;line-height:15px;color:#222}
.welcome-text p+p{margin-top:15px}
.btn-outline{left:106px;top:932px;width:181px;height:44px;border:1px solid #888;display:flex;align-items:center;justify-content:center;font-size:19px;color:#555}

.offers{left:0;top:1030px;width:1200px;height:476px;background:var(--grey-bg)}
.feature{left:107px;top:1056px;width:375px;height:375px;background:linear-gradient(170deg,#6f8b3a 0%,#5c6b35 40%,#4a3a2c 70%,#6b4e33 100%)}
.feature-title{left:107px;top:1272px;width:365px;text-align:right;color:var(--white);font-size:26px;line-height:32px}
.feature-sub{left:107px;top:1308px;width:367px;text-align:right;color:var(--white);font-size:14px;font-weight:700;line-height:18px}
.feature-btn{left:343px;top:1362px;width:126px;height:30px;background:rgba(255,255,255,.85);color:#222;font-style:italic;font-size:14px;display:flex;align-items:center;justify-content:center}
.card{top:1056px;width:175px}
.card-img{width:175px;height:175px}
.card-title{margin-top:27px;font-size:15px;line-height:18px;color:var(--wine)}
.card-desc{font-size:11px;line-height:13px;color:#333}
.card-price{margin-top:10px;font-size:18px;color:var(--wine)}
.card-btn{position:absolute;top:330px;left:0;width:175px;height:44px;background:var(--btn-grey);color:var(--white);font-style:italic;font-size:16px;display:flex;align-items:center;justify-content:center}
.dots{left:544px;top:1462px;width:550px;height:16px}

.cta{left:0;top:1506px;width:1200px;height:294px;background:linear-gradient(90deg,#b04a58,#a9303f 50%,#962331)}
.cta-title{left:229px;top:1545px;font-size:29px;font-weight:700;font-style:italic;line-height:37px;color:var(--white)}
.cta-text{left:229px;top:1652px;font-size:22px;font-weight:300;line-height:27px;color:var(--white)}
.cta-btn{left:692px;top:1699px;width:287px;height:43px;border:1px solid var(--white);color:var(--white);font-size:22px;font-style:italic;display:flex;align-items:center;justify-content:center}

.skyline{left:0;top:1845px;width:560px;height:127px;background:linear-gradient(180deg,rgba(161,28,40,.15),var(--wine))}
.footer{left:0;top:1972px;width:1200px;height:199px;background:var(--wine)}
.f-address,.f-phone,.f-menu,.copyright{color:var(--white)}
.f-address{left:250px;top:2004px;font-size:11.5px;line-height:14px}
.f-address .name{font-family:"Berkshire Swash",cursive;font-size:13px;line-height:16px}
.f-phone{left:250px;top:2070px;font-size:11.5px;line-height:14px}
.f-icon{left:228px}
.f-menu{top:2005px;font-size:11.5px;line-height:22px}
.f-menu h4{font-size:11.5px;font-weight:700;line-height:14px;margin-bottom:4px}
.social{left:739px;top:2013px;display:flex;gap:13px}
.social span{width:50px;height:50px;border-radius:50%;background:var(--white);display:block}
.f-rule{left:228px;top:2127px;width:749px;height:1px;background:rgba(255,255,255,.6)}
.copyright{left:0;top:2139px;width:1200px;text-align:center;font-size:11px;line-height:14px}
</style>
</head>
<body>
<div class="abs top-bar"></div>
<header class="abs header"></header>
<div class="abs brand"><span class="brand-mark"></span>Genusspfade</div>
<nav class="abs nav"><span class="active">Home</span><span>Shop</span><span>Menüpunkt</span><span>Menüpunkt</span><span>Kontakt</span></nav>
<svg class="abs search" width="28" height="28" viewBox="0 0 28 28"><circle cx="17" cy="11" r="7.5" fill="none" stroke="#111" stroke-width="2.5"/><line x1="11.5" y1="16.5" x2="3" y2="25" stroke="#111" stroke-width="3.5" stroke-linecap="round"/></svg>

<section class="abs hero" role="img" aria-label="Burg auf einem Weinberg mit Bäumen und Tal, rot getönt"></section>
<div class="abs hero-title script">Lorem Ipsum dolor</div>
<div class="abs hero-sub">ipsum dolor sit amet</div>
<div class="abs hero-btn">Lorem Ipsum</div>

<section class="abs welcome"></section>
<div class="abs welcome-photo" role="img" aria-label="Getreideähren und Hopfendolden auf weißem Holz"></div>
<h2 class="abs welcome-title script">Herzlich Willkommen</h2>
<div class="abs welcome-text">
<p>Wir lieben die Steiermark mit ihrem guten Essen, hervorragendem Bier und exquisitem Wein und möchten gerne anspruchsvolle Gäste verwöhnen. Als Start-up Unternehmen mit Sitz in Berlin und wollen wir unsere Begeisterung für die Steiermark mit ihren kulinarischen Spezialitäten, wunderschönen Landschaften und gastfreundlichen Menschen gern mit unseren Gästen teilen.<br>„Genusspfade“ ist daher auf der Suche nach Partnern, die mit uns unser neues Projekt in der Steiermark starten möchten.</p>
<p>Unser Ziel ist es, exklusive Klein-gruppenreisen mit kulinarischem Schwerpunkt in die Steiermark zu führen. Wir konzentrieren uns auf Geschäftsleute aus Berlin und Brandenburg, die unsere Reisen als Marketinginstrument für Kunden, im Rahmen der Wertschätzung von Mitarbeitern oder auch einfach nur privat nutzen möchten.</p>
</div>
<div class="abs btn-outline script">mehr lesen</div>

<section class="abs offers"></section>
<div class="abs feature" role="img" aria-label="Weinglas auf Holztisch im Weinberg mit Trauben und Walnüssen"></div>
<div class="abs feature-title script">Lorem Ipsum</div>
<div class="abs feature-sub">Finden Sie Ihr Geschmackserlebnis<br>in der Steiermark!</div>
<div class="abs feature-btn">Alle ansehen</div>

<article class="abs card" style="left:544px">
  <div class="card-img" role="img" aria-label="Weinreben mit Trauben vor Weinbergen" style="background:linear-gradient(135deg,#3f6a22,#7aa33a 60%,#c9d3c0)"></div>
  <div class="card-title script">Von Bier zu Wein</div>
  <div class="card-desc">Lorem ipsum dolor sit amet,<br>consetetur sadipscing elitr</div>
  <div class="card-price">199,00 - 249,00 €</div>
  <div class="card-btn">jetzt buchen</div>
</article>
<article class="abs card" style="left:731px">
  <div class="card-img" role="img" aria-label="Bunte Altstadthäuser mit Uhrturm und Brunnen" style="background:linear-gradient(180deg,#3f7fcf,#d0603a 40%,#b8543a 75%,#5a5a70)"></div>
  <div class="card-title script">Lorem Ipsum dolor</div>
  <div class="card-desc">Lorem ipsum dolor sit amet,<br>consetetur sadipscing elitr</div>
  <div class="card-price">199,00 - 249,00 €</div>
  <div class="card-btn">jetzt buchen</div>
</article>
<article class="abs card" style="left:918px">
  <div class="card-img" role="img" aria-label="Klarer Bergsee mit Felswänden und Wald" style="background:linear-gradient(180deg,#9ab7cf,#4d6a45 35%,#3b8fb0 55%,#7fb5c4 80%,#c9c5b8)"></div>
  <div class="card-title script">Lorem Ipsum dolor</div>
  <div class="card-desc">Lorem ipsum dolor sit amet,<br>consetetur sadipscing elitr</div>
  <div class="card-price">199,00 - 249,00 €</div>
  <div class="card-btn">jetzt buchen</div>
</article>
<svg class="abs dots" viewBox="0 0 550 16">
  <polyline points="8,1 1,8 8,15" fill="none" stroke="#111" stroke-width="1.5"/>
  <circle cx="55" cy="8" r="4" fill="#111"/>
  <g fill="#bbb"><circle cx="118" cy="8" r="4"/><circle cx="180" cy="8" r="4"/><circle cx="243" cy="8" r="4"/><circle cx="305" cy="8" r="4"/><circle cx="368" cy="8" r="4"/><circle cx="430" cy="8" r="4"/><circle cx="493" cy="8" r="4"/></g>
  <polyline points="542,1 549,8 542,15" fill="none" stroke="#111" stroke-width="1.5"/>
</svg>

<section class="abs cta" role="img" aria-label="Weintrauben am Rebstock, rot getönt"></section>
<h2 class="abs cta-title">Erleben Sie die<br>gastronomische Vielfalt der Süd-Steiermark</h2>
<p class="abs cta-text">Sie suchen ein bestimmtes Gaumenerlebnis?<br>Dann helfen wir Ihnen gerne weiter.</p>
<div class="abs cta-btn">Jetzt beraten lassen</div>

<div class="abs skyline" role="img" aria-label="Silhouette von Bergen und Stadt in Weinrot"></div>
<footer class="abs footer"></footer>
<svg class="abs f-icon" style="top:2006px" width="11" height="14" viewBox="0 0 11 14"><path d="M5.5 0A5 5 0 0 0 .5 5c0 3.5 5 9 5 9s5-5.5 5-9a5 5 0 0 0-5-5z" fill="#fff"/><circle cx="5.5" cy="5" r="1.8" fill="#a11c28"/></svg>
<div class="abs f-address"><div class="name">Genusspfade</div>Marlene Ostrach<br>Lindenhain 12<br>D - 10999 Berlin</div>
<svg class="abs f-icon" style="top:2071px" width="13" height="13" viewBox="0 0 13 13"><path d="M3 0l2 3-1.3 1.5a8 8 0 0 0 4.8 4.8L10 8l3 2-1.5 2.5C6 13 0 7 .5 1.5z" fill="#fff"/></svg>
<div class="abs f-phone">Deutschland: +49 170 0000 381<br>Österreich: +43 681 0000 7294</div>
<div class="abs f-menu" style="left:462px"><h4>MENÜ</h4>MENÜPUNKT<br>MENÜPUNKT<br>MENÜPUNKT<br>MENÜPUNKT</div>
<div class="abs f-menu" style="left:601px"><h4>MENÜ</h4>MENÜPUNKT<br>MENÜPUNKT<br>MENÜPUNKT<br>MENÜPUNKT</div>
<div class="abs social" aria-label="Soziale Netzwerke"><span></span><span></span><span></span><span></span></div>
<div class="abs f-rule"></div>
<div class="abs copyright">© 2017. Atelier Brennwald</div>
</body>
</html>
```